Veltrano Strom GmbH webpage The online Business card of a master electrician

A clean, modern webpage on whitch i can show my clients what im capable of and where the future costumer can inform himself. I need a login page for costumers who are registred and an secound webpage where my stuff can login to report theyr labour.
I will post pictures before and after, put on some commercial and crossellimg informations.
The costumer should find my insta as well my twitter or snapchat accounts.

Update:
Our Services are, Installations, Renovations, Home Automation, CCTV, Telefon / VOIP, Networking / Network-Cabeling, Electrical Supervisioning

Target Market(s)

Private and business costumers

Industry/Entity Type

Electric Company

Number of Pages Required

5+ page

Font styles to use
Sans Serif
Other font styles liked:
• Zurich,

Colors

Designer to choose colors to be used in the design.

Requirements
Must have
• A Page Hero
• A Costumer and staff login page (2separate pages)
• Contact form
• Responsive form
• Instagram enbedding account veltrano_strom
Nice to have
• A Blog

```html
<!DOCTYPE html>
<html lang="en">
<head>
<meta charset="utf-8">
<title>Veltrano Strom – Electrical Services</title>
<link href="https://fonts.googleapis.com/css2?family=Oswald:wght@400;500;600&family=Roboto:wght@300;400;500&display=swap" rel="stylesheet">
<style>
:root{
  --blue:#1aa3e0;
  --navy:#1a4f9c;
  --navy-dark:#143f85;
  --ink:#222;
  --muted:#8a8a8a;
  --line:#e3e3e3;
  --grey-bg:#f2f2f2;
  --white:#fff;
}
*{box-sizing:border-box;margin:0;padding:0}
html,body{width:727px;height:1200px;overflow:hidden;background:var(--white)}
body{position:relative;font-family:Roboto,sans-serif;color:var(--ink)}
.abs{position:absolute}
.head-font{font-family:Oswald,sans-serif}

/* hero */
.hero{left:0;top:0;width:727px;height:410px;background:linear-gradient(180deg,#1c2733 0%,#3a4450 30%,#6b5a4c 55%,#2d4560 70%,#1d3550 100%)}
.hero-curve{left:0;top:380px}
.brand{left:67px;top:16px;color:var(--white);font-family:Oswald,sans-serif;font-weight:600;font-size:19px;letter-spacing:1px;display:flex;align-items:center;gap:7px}
.brand-mark{width:12px;height:12px;background:var(--white)}
.phone{left:477px;top:12px;color:var(--white);display:flex;gap:6px;align-items:center}
.phone-num{font-size:12px;font-weight:300}
.phone-sub{font-size:7.5px}
.btn-enquiry{left:585px;top:12px;width:75px;height:23px;background:var(--blue);color:var(--white);font-family:Oswald,sans-serif;font-size:9px;display:flex;align-items:center;justify-content:center}
.nav-rule{left:0;top:49px;width:727px;height:1px;background:rgba(255,255,255,.2)}
.nav{left:67px;top:57px;display:flex;gap:21px;font-size:7.5px;color:var(--white)}
.nav .active{border-bottom:2px solid var(--blue);padding-bottom:8px}
.logins{left:512px;top:57px;display:flex;gap:10px;font-size:7.5px;color:var(--white)}
.hero-title{left:62px;top:222px;color:var(--white);font-family:Oswald,sans-serif;font-weight:600;font-size:31px;line-height:1.1}
.hero-sub{left:62px;top:258px;color:var(--white);font-family:Oswald,sans-serif;font-weight:500;font-size:17px}
.btn-call{left:62px;top:294px;width:113px;height:23px;background:var(--blue);color:var(--white);font-family:Oswald,sans-serif;font-size:9.5px;display:flex;align-items:center;justify-content:center}
.btn-services{left:181px;top:294px;width:92px;height:23px;border:1px solid var(--white);color:var(--white);font-family:Oswald,sans-serif;font-size:9.5px;display:flex;align-items:center;justify-content:center}

/* services */
.services-bg{left:0;top:410px;width:727px;height:165px;background:var(--grey-bg)}
.service{top:375px;width:100px;text-align:center}
.service-icon{width:60px;height:60px;margin:0 auto;border-radius:50%;background:radial-gradient(circle at 50% 35%,#2a86d8,#1a4f9c);border:3px solid var(--white);box-shadow:0 0 0 1px #cfe6f5;display:flex;align-items:center;justify-content:center}
.service h3{font-family:Oswald,sans-serif;font-weight:400;font-size:9.5px;height:26px;margin-top:12px;line-height:1.2}
.service .dash{width:14px;height:1px;background:var(--blue);margin:6px auto 8px}
.service p{font-size:7px;color:var(--muted);line-height:1.5;padding:0 4px}
.service .more{display:inline-block;margin-top:8px;border:1px solid #cfcfcf;font-size:6px;padding:3px 5px;background:var(--white)}

/* mid */
.col-title{font-family:Oswald,sans-serif;font-weight:500;font-size:12px}
.col-rule{height:1px;background:var(--line)}
.col-rule::before{content:"";display:block;width:50px;height:2px;background:var(--navy)}
.insta-grid{left:67px;top:638px;display:grid;grid-template-columns:repeat(3,59px);gap:5px 5px}
.tile{width:59px;height:59px}
.insta-handle{left:67px;top:835px;width:188px;text-align:center;font-size:6.5px;color:var(--navy)}
.form-panel{left:270px;top:605px;width:187px;height:237px;background:#f0f0f0}
.form-head{left:270px;top:605px;width:187px;height:60px}
.form-title{left:286px;top:617px;color:var(--white);display:flex;gap:6px;align-items:center}
.field{left:286px;width:155px;height:21px;background:var(--white);border:1px solid #e6e6e6;font-size:7.5px;color:#999;padding:5px 6px}
.btn-submit{left:286px;top:804px;width:155px;height:21px;background:var(--blue);color:var(--white);font-size:8px;display:flex;align-items:center;justify-content:center}
.post{left:472px;width:188px}
.post h4{font-size:8.5px;font-weight:400;line-height:1.35}
.post .meta{font-size:5.8px;color:#777;margin-top:4px}
.post .meta b{color:var(--blue);font-weight:400}
.post p{font-size:7px;color:var(--muted);line-height:1.5;margin-top:7px}
.view-more{left:472px;top:834px;width:188px;text-align:center;font-size:6px;color:#555}

/* why */
.section-rule{left:0;top:872px;width:727px;height:1px;background:var(--line)}
.why-title{left:0;top:900px;width:727px;text-align:center;font-family:Oswald,sans-serif;font-weight:500;font-size:12px}
.why{top:932px;width:135px}
.why-top{display:flex;gap:8px;align-items:center}
.why-top span{font-size:8.5px;line-height:1.3}
.why p{font-size:7px;color:var(--muted);line-height:1.5;margin-top:12px}

/* footer */
.footer{left:0;top:1033px;width:727px;height:142px;background:var(--navy)}
.foot-bar{left:0;top:1175px;width:727px;height:25px;background:var(--navy-dark);color:#b9cbe8;font-size:7px;display:flex;align-items:center;justify-content:center}
.foot-h{font-family:Oswald,sans-serif;font-size:8.5px;color:var(--white)}
.foot-t{font-size:7px;color:#b9cbe8;line-height:1.6}
.subscribe{left:523px;top:1070px;width:137px;height:20px;background:var(--white);border-radius:10px;font-size:7px;color:#999;padding:6px 11px}
.sub-go{left:643px;top:1073px;width:14px;height:14px;border-radius:50%;background:var(--blue)}
.socials{left:523px;top:1127px;display:flex;gap:4px}
.socials span{width:17px;height:17px;border:1px solid #b9cbe8;border-radius:50%}
</style>
</head>
<body>

<!-- hero -->
<div class="abs hero" role="img" aria-label="Evening photo of a lakeside old town with church spires reflected in the water"></div>
<svg class="abs hero-curve" width="727" height="40" viewBox="0 0 727 40">
  <path d="M0 20 Q363 0 727 20 L727 40 L0 40 Z" fill="#f2f2f2"/>
  <path d="M0 20 Q363 0 727 20" fill="none" stroke="#1aa3e0" stroke-width="3"/>
</svg>

<div class="abs brand"><span class="brand-mark"></span>VELTRANO STROM</div>
<div class="abs phone">
  <svg width="10" height="17" viewBox="0 0 10 17"><rect x="1" y="1" width="8" height="15" rx="1.5" fill="none" stroke="#1aa3e0" stroke-width="1.4"/><circle cx="5" cy="13" r="0.9" fill="#1aa3e0"/></svg>
  <div><div class="phone-num">1-800-555-0142</div><div class="phone-sub">Call 24/7 Hours Support</div></div>
</div>
<div class="abs btn-enquiry">ENQUIRY NOW!</div>
<div class="abs nav-rule"></div>
<nav class="abs nav">
  <span class="active">HOME</span><span>ABOUT US</span><span>SERVICES</span><span>TESTIMONIALS</span><span>BLOG</span><span>CONTACT US</span>
</nav>
<div class="abs logins"><span>● CUSTOMER LOGIN</span><span>● STAFF LOGIN</span></div>

<div class="abs hero-title">VELTRANO STROM</div>
<div class="abs hero-sub">LEADING PROVIDER ELECTRICAL SERVICES</div>
<div class="abs btn-call">REQUEST A CALL BACK</div>
<div class="abs btn-services">SEE ALL SERVICES</div>

<!-- services -->
<div class="abs services-bg"></div>

<div class="abs service" style="left:60px">
  <div class="service-icon"><svg width="24" height="24" viewBox="0 0 24 24" fill="none" stroke="#fff" stroke-width="2"><circle cx="12" cy="12" r="9"/><path d="M9 7v4M15 7v4M8 11h8v2a4 4 0 0 1-8 0z"/></svg></div>
  <h3>INSTALLATIONS</h3><div class="dash"></div>
  <p>Duis sed odio sit amet nibh vulputate cursus a sit amet mauris. Morbi ipsum velit.</p><span class="more">READ MORE</span>
</div>
<div class="abs service" style="left:161px">
  <div class="service-icon"><svg width="24" height="24" viewBox="0 0 24 24" fill="none" stroke="#fff" stroke-width="2"><path d="M5 19L14 10M15 4a4 4 0 0 0 5 5l-3 3-5-5zM5 5l14 14"/></svg></div>
  <h3>RENOVATIONS</h3><div class="dash"></div>
  <p>Duis sed odio sit amet nibh vulputate cursus a sit amet mauris. Morbi ipsum velit.</p><span class="more">READ MORE</span>
</div>
<div class="abs service" style="left:263px">
  <div class="service-icon"><svg width="24" height="24" viewBox="0 0 24 24" fill="none" stroke="#fff" stroke-width="2"><path d="M3 12L12 4l9 8M6 10v10h12V10"/><circle cx="12" cy="15" r="2"/></svg></div>
  <h3>HOME<br>AUTOMATION</h3><div class="dash"></div>
  <p>Duis sed odio sit amet nibh vulputate cursus a sit amet mauris. Morbi ipsum velit.</p><span class="more">READ MORE</span>
</div>
<div class="abs service" style="left:364px">
  <div class="service-icon"><svg width="24" height="24" viewBox="0 0 24 24" fill="none" stroke="#fff" stroke-width="2"><path d="M4 7l13 4-2 4-11-4zM10 13v5H5"/></svg></div>
  <h3>CCTV</h3><div class="dash"></div>
  <p>Duis sed odio sit amet nibh vulputate cursus a sit amet mauris. Morbi ipsum velit.</p><span class="more">READ MORE</span>
</div>
<div class="abs service" style="left:465px">
  <div class="service-icon"><svg width="24" height="24" viewBox="0 0 24 24" fill="none" stroke="#fff" stroke-width="2"><rect x="4" y="10" width="9" height="8" rx="1"/><path d="M13 14c4 0 4-8 8-8M7 10V7M10 10V7"/></svg></div>
  <h3>NETWORK<br>CABELING</h3><div class="dash"></div>
  <p>Duis sed odio sit amet nibh vulputate cursus a sit amet mauris. Morbi ipsum velit.</p><span class="more">READ MORE</span>
</div>
<div class="abs service" style="left:566px">
  <div class="service-icon"><svg width="24" height="24" viewBox="0 0 24 24" fill="none" stroke="#fff" stroke-width="2"><path d="M5 14a7 7 0 0 1 14 0zM3 14h18M12 7v4M8 18h8v3H8z"/></svg></div>
  <h3>ELECTRICAL<br>SUPERVISIONING</h3><div class="dash"></div>
  <p>Duis sed odio sit amet nibh vulputate cursus a sit amet mauris. Morbi ipsum velit.</p><span class="more">READ MORE</span>
</div>

<!-- instagram -->
<div class="abs col-title" style="left:67px;top:602px">FOLLOW ON INSTAGRAM</div>
<div class="abs" style="left:245px;top:606px;width:9px;height:9px;background:#5b8fd1;border-radius:2px"></div>
<div class="abs col-rule" style="left:67px;top:626px;width:188px"></div>
<div class="abs insta-grid">
  <div class="tile" role="img" aria-label="Restaurant interior with set tables" style="background:linear-gradient(135deg,#6b5844,#c9b89a)"></div>
  <div class="tile" role="img" aria-label="Dining room with warm pendant lights" style="background:linear-gradient(135deg,#3b2e22,#d6a642)"></div>
  <div class="tile" role="img" aria-label="Old town skyline at dusk" style="background:linear-gradient(180deg,#7c8ea8,#3c4d6a)"></div>
  <div class="tile" role="img" aria-label="Dining room with warm pendant lights" style="background:linear-gradient(135deg,#3b2e22,#d6a642)"></div>
  <div class="tile" role="img" aria-label="Aerial view of a house among trees" style="background:linear-gradient(135deg,#5d7a4a,#b9b4a2)"></div>
  <div class="tile" role="img" aria-label="Restaurant interior with warm lighting" style="background:linear-gradient(135deg,#3b2e22,#c98f3a)"></div>
  <div class="tile" role="img" aria-label="Aerial view of a house among trees" style="background:linear-gradient(135deg,#5d7a4a,#b9b4a2)"></div>
  <div class="tile" role="img" aria-label="Old town skyline at dusk" style="background:linear-gradient(180deg,#8a9ab4,#3c4d6a)"></div>
  <div class="tile" role="img" aria-label="Restaurant interior with set tables" style="background:linear-gradient(135deg,#6b5844,#d6cbb6)"></div>
</div>
<div class="abs insta-handle">@VELTRANO_STROM</div>

<!-- request form -->
<div class="abs form-panel"></div>
<svg class="abs form-head" width="187" height="60" viewBox="0 0 187 60">
  <path d="M0 0H187V55L0 50Z" fill="#1aa3e0"/>
  <path d="M0 50L187 55V60L0 58Z" fill="#1a4f9c"/>
</svg>
<div class="abs form-title">
  <span style="width:10px;height:10px;background:#fff"></span>
  <div><div class="head-font" style="font-size:14px;font-weight:600;line-height:1">REQUEST</div><div style="font-size:8px;letter-spacing:2px">A CALL BACK</div></div>
</div>
<div class="abs field" style="top:675px">Name</div>
<div class="abs field" style="top:702px">Email</div>
<div class="abs field" style="top:729px">Phone</div>
<div class="abs field" style="top:756px;height:40px">Message</div>
<div class="abs btn-submit">SUBMIT</div>

<!-- blog -->
<div class="abs col-title" style="left:472px;top:602px">LATEST BLOG</div>
<svg class="abs" style="left:647px;top:605px" width="13" height="11" viewBox="0 0 13 11"><path d="M1 1h11v7H5l-3 3V8H1z" fill="#8a9ab4"/></svg>
<div class="abs col-rule" style="left:472px;top:626px;width:188px"></div>
<div class="abs post" style="top:638px">
  <h4>Professional lorem ipsum generator for used as typographers Webpage</h4>
  <div class="meta">By <b>Lena Hartmann</b> | 23 May 2017 | 20 Comments</div>
  <p>Duis sed odio sit amet nibh vulputate cursus a sit amet mauris. Morbi duis sed odio sit amet nibh vulputate ipsum velit.</p>
</div>
<div class="abs" style="left:472px;top:720px;width:188px;height:1px;background:var(--line)"></div>
<div class="abs post" style="top:742px">
  <h4>Professional lorem ipsum generator for used as typographers Webpage</h4>
  <div class="meta">By <b>Lena Hartmann</b> | 23 May 2017 | 20 Comments</div>
  <p>Duis sed odio sit amet nibh vulputate cursus a sit amet mauris. Morbi duis sed odio sit amet nibh vulputate ipsum velit.</p>
</div>
<div class="abs" style="left:472px;top:824px;width:188px;height:1px;background:var(--line)"></div>
<div class="abs view-more">VIEW MORE BLOGS ▸</div>

<!-- why choose us -->
<div class="abs section-rule"></div>
<div class="abs why-title">WHY CHOOSE US</div>
<div class="abs why" style="left:67px">
  <div class="why-top"><svg width="26" height="22" viewBox="0 0 26 22"><path d="M6 1h14l5 6-12 14L1 7z" fill="#1a6fd0"/></svg><span>Quality Services for<br>Over 20 Years</span></div>
  <p>Duis sed odio sit amet nibh vulputate cursus a sit amet mauris. Morbi duis sed nibh vulputate ipsum velit.</p>
</div>
<div class="abs why" style="left:219px">
  <div class="why-top"><svg width="26" height="24" viewBox="0 0 26 24"><circle cx="13" cy="12" r="11" fill="#1a6fd0"/><path d="M8 12l4 4 6-8" fill="none" stroke="#fff" stroke-width="2.2"/></svg><span>Licensed Master<br>Electrician</span></div>
  <p>Duis sed odio sit amet nibh vulputate cursus a sit amet mauris. Morbi duis sed nibh vulputate ipsum velit.</p>
</div>
<div class="abs why" style="left:371px">
  <div class="why-top"><svg width="26" height="22" viewBox="0 0 26 22"><path d="M13 21L3 11a5.5 5.5 0 0 1 10-6 5.5 5.5 0 0 1 10 6z" fill="#1a6fd0"/></svg><span>We Love<br>Our Customers</span></div>
  <p>Duis sed odio sit amet nibh vulputate cursus a sit amet mauris. Morbi duis sed nibh vulputate ipsum velit.</p>
</div>
<div class="abs why" style="left:523px">
  <div class="why-top"><svg width="26" height="24" viewBox="0 0 26 24"><path d="M5 3h5l2 6-3 2a12 12 0 0 0 5 5l2-3 6 2v5c-11 1-18-6-17-17z" fill="#1a6fd0"/></svg><span>24/7 Customer<br>Support Helpline</span></div>
  <p>Duis sed odio sit amet nibh vulputate cursus a sit amet mauris. Morbi duis sed nibh vulputate ipsum velit.</p>
</div>

<!-- footer -->
<div class="abs footer"></div>
<div class="abs foot-h" style="left:67px;top:1051px">RECENT BLOG POSTS</div>
<div class="abs foot-t" style="left:67px;top:1068px;width:145px">
  <div style="font-size:6px">20 May 2017</div>
  <div>Lorem Ipsum is simply dummy text of the printing typesetting industry.</div>
  <div style="font-size:6px;margin-top:9px">20 May 2017</div>
  <div>Lorem Ipsum is simply dummy text of the printing typesetting industry.</div>
</div>
<div class="abs foot-h" style="left:262px;top:1051px">CONTACT DETAILS</div>
<div class="abs foot-t" style="left:262px;top:1068px;width:130px">
  Veltrano Strom<br>42 Birchfield Lane, Austin,<br>Texas 73301<br><br>T: 1800 555 0142<br>F: 1800 555 0143<br>E: info@veltranostrom.com
</div>
<div class="abs foot-h" style="left:415px;top:1051px">QUICK LINKS</div>
<div class="abs foot-t" style="left:415px;top:1068px;line-height:1.75">Home<br>About Us<br>Services<br>Testimonials<br>Blog<br>Contact Us</div>
<div class="abs foot-h" style="left:523px;top:1051px">SUBSCRIBE NEWSLETTER</div>
<div class="abs subscribe">Email Address</div>
<div class="abs sub-go"></div>
<div class="abs foot-h" style="left:523px;top:1109px">STAY CONNECTED</div>
<div class="abs socials"><span></span><span></span><span></span><span></span><span></span></div>
<div class="abs foot-bar">Copyright ©2017 Veltrano Strom. Terms of Use | Privacy Policy | Sitemap</div>

</body>
</html>
```